Velvet Evening Soirée Flyer for a female oriented event

I need a flyer to promote my event which should look "FUN" and "Sophisticated"
I would need the flyer to be 8 1/2" X 11" 300 dpi. I would need the layered .psd file as well as all the fonts. The flyer should contain the following info:

Velvet Evening Soirée CT
Friday, September 25th
6:00-10:00 PM
The Jasper Hall Pavilion
7 Orwell Ln
Danbury, CT 06811
First 100 guests will have a chance to win $25,000 and receive a swag bag filled with gifts
$20 Advanced Admission at www.velveteveningsoireect.example
$25 at the door
(Key words)
Martini Bar
Wine Tasting
Food Sampling
Beauty Make-Overs
Fashion Shows
Psychic Readings
Shopping
Door Prizes
Swag Bag
Exhibitors
For tickets visit www.velveteveningsoireect.example

Target Market(s)

Ladies

Industry/Entity Type

Event

Requirements
Must have
• see description

```html
<!DOCTYPE html>
<html lang="en">
<head>
<meta charset="utf-8">
<title>Velvet Evening Soirée CT – Flyer</title>
<link rel="stylesheet" href="https://fonts.googleapis.com/css2?family=Antonio:wght@400;500&family=Roboto+Condensed:wght@400;700&display=swap">
<style>
  :root {
    --page: #e4e4e6;
    --ink: #000000;
    --coral: #e9504a;
    --olive: #4a4a3f;
    --sand: #c9bd98;
    --sand-light: #d8cca8;
    --white: #ffffff;
    --dark-text: #1b1414;
  }
  * { box-sizing: border-box; margin: 0; padding: 0; }
  html, body {
    width: 969px; height: 1200px; overflow: hidden;
    background: var(--page);
  }
  .flyer {
    position: absolute; left: 66px; top: 15px;
    width: 836px; height: 1170px;
    background: var(--ink);
    overflow: hidden;
    font-family: "Roboto Condensed", "Arial Narrow", sans-serif;
  }
  .hero-photo {
    position: absolute; left: 368px; top: 0; width: 468px; height: 627px;
    background:
      radial-gradient(ellipse 45% 40% at 50% 30%, #3a3230 0%, rgba(20,18,18,0) 70%),
      radial-gradient(ellipse 50% 35% at 55% 75%, #2f2e26 0%, rgba(0,0,0,0) 75%),
      #050505;
  }
  .party-art {
    position: absolute; left: 0; top: 557px; width: 312px; height: 613px;
    background:
      radial-gradient(ellipse 70% 35% at 35% 30%, rgba(233,80,74,.55) 0%, rgba(233,80,74,0) 70%),
      radial-gradient(ellipse 80% 45% at 45% 85%, rgba(233,80,74,.85) 0%, rgba(233,80,74,0) 75%),
      var(--ink);
  }
  .title {
    position: absolute; right: 465px; top: 70px;
    text-align: right;
    font-family: "Antonio", "Oswald", sans-serif;
    font-weight: 500;
    text-transform: uppercase;
    line-height: 1;
    white-space: nowrap;
  }
  .title span { display: block; font-size: 116px; letter-spacing: -2px; line-height: 134px; }
  .title .t-1 { color: var(--coral); }
  .title .t-2 { color: var(--olive); }
  .title .t-3 { color: var(--sand); }
  .title .t-4 { color: var(--sand-light); font-size: 64px; line-height: 72px; margin-top: -4px; }
  .event-date {
    position: absolute; left: 371px; top: 640px; width: 465px;
    color: var(--coral);
    font-weight: 700; font-size: 20px; line-height: 27px;
    text-transform: uppercase;
  }
  .venue {
    position: absolute; left: 371px; top: 668px; width: 465px;
    color: var(--sand-light);
    font-weight: 700; font-size: 20px; line-height: 27px;
    text-transform: uppercase;
  }
  .ticket {
    position: absolute; left: 371px; top: 738px; width: 465px; height: 231px;
    background: var(--coral);
    padding: 26px 24px 0 34px;
  }
  .ticket::before {
    content: ""; position: absolute; inset: 0;
    background:
      radial-gradient(circle at 0 50%, var(--ink) 4px, transparent 4.6px) left top / 10px 13px repeat-y,
      radial-gradient(circle at 100% 50%, var(--ink) 4px, transparent 4.6px) right top / 10px 13px repeat-y,
      radial-gradient(circle at 50% 0, var(--ink) 4px, transparent 4.6px) left top / 13px 10px repeat-x,
      radial-gradient(circle at 50% 100%, var(--ink) 4px, transparent 4.6px) left bottom / 13px 10px repeat-x;
  }
  .ticket::after {
    content: ""; position: absolute; inset: 14px;
    border: 2px solid var(--dark-text);
  }
  .ticket-offer {
    color: var(--dark-text); font-weight: 700; font-size: 19.5px; line-height: 26px;
    text-transform: uppercase; position: relative;
  }
  .ticket-price {
    color: var(--white); font-weight: 700; font-size: 18px; line-height: 26px;
    margin-top: 8px; position: relative;
  }
  .features {
    position: absolute; left: 375px; top: 988px; width: 461px;
    color: var(--white); font-weight: 700; font-size: 14.5px; line-height: 21px;
    text-transform: uppercase;
  }
  .tickets-label {
    position: absolute; left: 375px; top: 1068px;
    color: var(--sand-light); font-size: 19px;
  }
  .tickets-url {
    position: absolute; left: 375px; top: 1098px;
    color: var(--sand-light); font-weight: 700; font-size: 30px;
    white-space: nowrap;
  }
</style>
</head>
<body>
  <main class="flyer">
    <div class="hero-photo" role="img" aria-label="Moody photograph of a woman holding a lipstick with several hands offering cosmetics, lit against a black background"></div>
    <div class="party-art" role="img" aria-label="Coral silhouettes of dancing women beneath a spray of coral bubbles"></div>

    <h1 class="title">
      <span class="t-1">Velvet</span>
      <span class="t-2">Evening</span>
      <span class="t-3">Soirée</span>
      <span class="t-4">CT</span>
    </h1>

    <p class="event-date">Friday, September 25th | 6:00-10:00 PM</p>
    <p class="venue">The Jasper Hall Pavilion 7 Orwell Ln,<br>Danbury, CT 06811</p>

    <section class="ticket">
      <p class="ticket-offer">First 100 guests will have a chance to<br>win $25,000 and receive<br>a swag bag filled with gifts</p>
      <p class="ticket-price">$20 Advanced Admission at<br>www.velveteveningsoireect.example<br>$25 at the door</p>
    </section>

    <p class="features">
      Martini Bar | Wine Tasting | Food Sampling<br>
      Beauty Make-Overs | Fashion Shows | Psychic Readings<br>
      Shopping | Door Prizes | Swag Bag | Exhibitors
    </p>

    <p class="tickets-label">For tickets visit</p>
    <p class="tickets-url">www.velveteveningsoireect.example</p>
  </main>
</body>
</html>
```